CD Cover Art for Breakout Album

I'm looking for cover art for my album that is in the "Americana" genre. It has some songs that are a little towards hard rock, but a couple are softer ballads as well. The album is called "Lanterns, Orchards, and Harvests," focusing on the after-effects of combat on the ones that serve. I want to integrate red, white and blue themes that are not pandering or kitchy. If possible, I would like to subtly integrate the "battlefield cross" which is attached as an image. I would like it to be as simple as possible, and don't want it solely military focused because the album is a collection of stories, only a few of which are explicitly military.

```html
<!DOCTYPE html>
<html lang="en">
<head>
<meta charset="utf-8">
<title>Lanterns, Orchards, and Harvests — Album Cover</title>
<link rel="stylesheet" href="https://fonts.googleapis.com/css2?family=Oswald:wght@700&display=swap">
<style>
  :root {
    --flag-red: #ff1205;
    --flag-blue: #0f3f87;
    --pale-blue: #e9f4f8;
    --paper-top: #ffffff;
    --paper-bottom: #e6e6e6;
    --emblem-grey: #d8d8d8;
    --title-shadow: rgba(0, 0, 0, 0.35);
  }
  * { margin: 0; padding: 0; box-sizing: border-box; }
  html, body {
    width: 1200px;
    height: 1199px;
    overflow: hidden;
    background: var(--paper-top);
  }
  .album-cover {
    position: relative;
    width: 1200px;
    height: 1199px;
    background: linear-gradient(200deg, var(--paper-top) 45%, var(--paper-bottom) 100%);
    overflow: hidden;
  }
  .flag-banner {
    position: absolute;
    inset: 0;
    width: 1200px;
    height: 1199px;
  }
  .memorial-emblem {
    position: absolute;
    left: 842px;
    top: 345px;
    width: 276px;
    height: 725px;
    border-radius: 120px 120px 30px 30px;
    background: linear-gradient(180deg, var(--emblem-grey), #e2e2e2);
    opacity: 0.85;
  }
  .album-title {
    position: absolute;
    left: 85px;
    top: 532px;
    font-family: "Oswald", "Arial Narrow", sans-serif;
    font-weight: 700;
    font-size: 146px;
    line-height: 184px;
    letter-spacing: -2px;
    text-transform: uppercase;
    text-shadow: 3px 3px 0 var(--title-shadow);
    white-space: nowrap;
  }
  .album-title .line { display: block; }
  .album-title .line--blue { color: var(--flag-blue); }
  .album-title .line--red { color: var(--flag-red); }
</style>
</head>
<body>
  <main class="album-cover">
    <svg class="flag-banner" viewBox="0 0 1200 1199">
      <defs>
        <linearGradient id="flagTones" x1="0" y1="0.6" x2="1" y2="0.2">
          <stop offset="0" stop-color="var(--flag-red)"/>
          <stop offset="0.5" stop-color="var(--pale-blue)"/>
          <stop offset="1" stop-color="var(--flag-blue)"/>
        </linearGradient>
      </defs>
      <polygon class="flag-area" points="0,0 1200,0 1200,381 0,516" fill="url(#flagTones)" role="img" aria-label="Angled red and white flag stripes meeting a starred blue canton in the top corner"/>
    </svg>

    <div class="memorial-emblem" role="img" aria-label="Faint grey battlefield cross: helmet on rifle with dog tags above boots"></div>

    <h1 class="album-title">
      <span class="line line--blue">Lanterns,</span>
      <span class="line line--red">Orchards &amp;</span>
      <span class="line line--blue">Harvests</span>
    </h1>
  </main>
</body>
</html>
```